Steadfast MD - Sleep Medicine Specialist - Business Cards

We are a new medical practice called Steadfast MD. We are sleep medicine specialists and we will be conducting sleep studies on patients with sleep related ailments. We want the business card to be bold, professional, and clean with the logo as the stand out visual piece. We dont like wild flashy designs. We want our design to be bold and classic while at the same time conveying who we are and what we do. We are reliable, professional, and the best in the business.

Industry/Entity Type

Health Care

Contact Information for Business Card

- Clean
- Bold
- Classic
- not cluttered

Requirements
Must have
• logo, website, phone number
Nice to have
• several options to choose from
Should not have
• flashy imaged - reflective print - images of people sleeping

```html
<!DOCTYPE html>
<html lang="en">
<head>
<meta charset="utf-8">
<title>Steadfast MD – Business Card</title>
<link href="https://fonts.googleapis.com/css2?family=Open+Sans:wght@400;700&display=swap" rel="stylesheet">
<style>
  :root {
    --backdrop: #e4e4e4;
    --card-dark: #060608;
    --card-light: #f4f4f4;
    --brand-red: #e31e24;
    --ink: #111111;
  }
  * { margin: 0; padding: 0; box-sizing: border-box; }
  html, body {
    width: 1200px; height: 960px; overflow: hidden;
    background: var(--backdrop);
    font-family: "Open Sans", Arial, sans-serif;
  }
  .canvas { position: relative; width: 1200px; height: 960px; }

  .card { position: absolute; left: 297px; width: 605px; height: 346px; overflow: hidden; }

  .card-front {
    top: 114px; background: var(--card-dark);
    display: flex; align-items: center; justify-content: center;
  }
  .front-name {
    color: var(--brand-red); font-weight: 700; font-size: 46px; letter-spacing: -0.5px;
  }

  .card-back { top: 514px; background: var(--card-light); }

  .brand { position: absolute; left: 37px; top: 40px; display: flex; align-items: center; gap: 8px; }
  .brand-mark {
    width: 66px; height: 66px; border-radius: 50%;
    border: 3px solid var(--brand-red);
  }
  .brand-name { color: var(--ink); font-weight: 700; font-size: 31px; letter-spacing: -1px; }

  .person { position: absolute; right: 37px; top: 166px; text-align: right; }
  .person-name { color: var(--brand-red); font-weight: 700; font-size: 18px; line-height: 24px; }
  .person-title { color: var(--ink); font-size: 14px; line-height: 22px; }

  .divider { position: absolute; left: 37px; right: 37px; top: 225px; height: 1.5px; background: var(--ink); }

  .contacts { position: absolute; left: 37px; top: 248px; list-style: none; }
  .contacts li {
    display: flex; align-items: center; gap: 6px;
    color: var(--ink); font-size: 14px; line-height: 20.5px;
  }
  .contacts svg { width: 14px; height: 14px; flex: none; }

  .footer-band { position: absolute; left: 0; bottom: 0; width: 570px; height: 15px; background: var(--card-dark); }
  .footer-accent { position: absolute; right: 0; bottom: 0; width: 32px; height: 15px; background: var(--brand-red); }
</style>
</head>
<body>
<main class="canvas">
  <section class="card card-front" aria-label="Card front">
    <span class="front-name">Steadfast MD</span>
  </section>

  <section class="card card-back" aria-label="Card back">
    <div class="brand">
      <span class="brand-mark"></span>
      <span class="brand-name">Steadfast MD</span>
    </div>

    <div class="person">
      <p class="person-name">DANIEL CARTER</p>
      <p class="person-title">Managing Director</p>
    </div>

    <div class="divider"></div>

    <ul class="contacts">
      <li>
        <svg viewBox="0 0 16 16"><path fill="#e31e24" d="M3.6 1.2l2.3 2.6-1.3 1.9c.9 2 2.4 3.6 4.5 4.6l1.9-1.3 2.7 2.2-1.4 2.4C7 13.4 2.6 9 1.4 2.6z"/></svg>
        <span>(555) 014-2837</span>
      </li>
      <li>
        <svg viewBox="0 0 16 16"><rect x="1.5" y="3.5" width="13" height="9" fill="none" stroke="#e31e24" stroke-width="1.6"/><path d="M1.5 3.5L8 9l6.5-5.5M1.5 12.5l5-4.5M14.5 12.5l-5-4.5" fill="none" stroke="#e31e24" stroke-width="1.4"/></svg>
        <span>daniel@steadfastmd.com</span>
      </li>
      <li>
        <svg viewBox="0 0 16 16"><g fill="none" stroke="#e31e24" stroke-width="1.3"><circle cx="8" cy="8" r="6.3"/><ellipse cx="8" cy="8" rx="2.8" ry="6.3"/><path d="M1.7 8h12.6M2.8 4.8h10.4M2.8 11.2h10.4"/></g></svg>
        <span>www.steadfastmd.com</span>
      </li>
    </ul>

    <div class="footer-band"></div>
    <div class="footer-accent"></div>
  </section>
</main>
</body>
</html>
```